Logo alteration and design business card.

I want to make minor alterations to a logo that has already been designed and use the modified logo as part of the design of the business card.

Alterations to be made are as follows:
16-6240 TPX For the top green and bottom green dot.
16-4535 TPX For the Bottom blue and top blue dot
13-0220 TPX For the green outline.
13-5313 TPX For the middle line and the writing.

Particulars such as name, phone number and email to be generic for now so we can update and individualize them later. Website is www.orbivale.com.au

Target Market(s)

Men and Women 25-35 interested in ecofriendly/green products that have a positive vibe and message.

Industry/Entity Type

Business

Font styles to use
Script

Colors
0492cd
85cae6
00a98f
86cfc6

Requirements
Must have
• The modified Lumora Vista logo.
Nice to have
• We're looking for a design that is either nature based eg. bamboo, birds, trees, water, natural scenery etc. or something eg. spacey, stars, galaxy, universe etc. a positive/happy feeling to it that is quite simple and not over loaded with imagery.

```html
<!DOCTYPE html>
<html lang="en">
<head>
<meta charset="utf-8">
<title>Lumora Vista – Business Card</title>
<link rel="stylesheet" href="https://fonts.googleapis.com/css2?family=Questrial&family=Arimo&display=swap">
<style>
  :root {
    --backdrop: #584e46;
    --card-white: #fafafa;
    --lime: #a9c934;
    --lime-deep: #9bc23a;
    --brand-green: #8cb43a;
    --white: #ffffff;
    --contact-ink: #7f9a3a;
    --label-ink: #ffffff;
  }
  * { margin: 0; padding: 0; box-sizing: border-box; }
  html, body {
    width: 1080px;
    height: 1200px;
    overflow: hidden;
    background: var(--backdrop);
  }
  .canvas {
    position: relative;
    width: 1080px;
    height: 1200px;
    background: var(--backdrop);
    font-family: "Questrial", sans-serif;
  }
  .card-side {
    position: absolute;
    left: 284px;
    width: 485px;
    height: 291px;
  }
  .card-front {
    top: 256px;
    background: var(--card-white);
    border-bottom: 1px solid #8a8a7a;
  }
  .card-back {
    top: 547px;
    background: linear-gradient(180deg, var(--lime) 0%, #a6c837 50%, var(--lime-deep) 100%);
    overflow: hidden;
  }
  .card-back .lower-band {
    position: absolute;
    left: 0; right: 0;
    top: 168px; bottom: 0;
    background: rgba(140, 185, 50, 0.25);
  }
  .brand-lockup {
    position: absolute;
    left: 0; right: 0;
    top: 96px;
    display: flex;
    align-items: center;
    justify-content: center;
    gap: 12px;
  }
  .brand-dot {
    width: 30px;
    height: 30px;
    border-radius: 50%;
    background: var(--brand-green);
    flex: none;
  }
  .brand-text { display: flex; flex-direction: column; }
  .brand-name {
    font-size: 34px;
    line-height: 1;
    color: var(--brand-green);
  }
  .brand-url {
    font-size: 13px;
    color: var(--brand-green);
    margin-top: 4px;
    text-align: right;
  }
  .back-name {
    position: absolute;
    left: 0; right: 0;
    top: 71px;
    text-align: center;
    font-size: 41px;
    line-height: 1;
    color: var(--white);
  }
  .back-url {
    position: absolute;
    left: 0; right: 0;
    top: 114px;
    text-align: center;
    font-size: 16px;
    color: var(--white);
  }
  .contact-list {
    position: absolute;
    left: 164px;
    top: 147px;
    list-style: none;
    font-size: 11px;
    line-height: 16px;
    color: var(--contact-ink);
  }
  .side-label {
    position: absolute;
    left: 823px;
    font-family: "Arimo", sans-serif;
    font-size: 52px;
    letter-spacing: 2px;
    color: var(--label-ink);
    line-height: 1;
  }
  .label-front { top: 396px; }
  .label-back { top: 606px; }
</style>
</head>
<body>
<div class="canvas">
  <section class="card-side card-front">
    <div class="brand-lockup">
      <span class="brand-dot"></span>
      <div class="brand-text">
        <span class="brand-name">Lumora Vista</span>
        <span class="brand-url">www.orbivale.com.au</span>
      </div>
    </div>
  </section>

  <section class="card-side card-back">
    <div class="lower-band"></div>
    <h1 class="back-name">Lumora Vista</h1>
    <p class="back-url">www.orbivale.com.au</p>
    <ul class="contact-list">
      <li>tel.: 123 456 7890</li>
      <li>fax: 123 456 7891</li>
      <li>email: info@</li>
    </ul>
  </section>

  <span class="side-label label-front">Front</span>
  <span class="side-label label-back">Back</span>
</div>
</body>
</html>
```